IT Consultant specialising in Orlo support and repairs needs new business card design

Looking for modern clean card design with new logo element for IT business. Specialising in Orlo products so looking for a design/logo element that will be immediately recognisable. Would also like social media icons to convey alternate communication avenues are available. PavLora, Quibbit, WorkNest as well as traditional Address, Phone, Email and Website.
Target Market(s)
Local Area Consumer and Business clientele
Industry/Entity Type
Communication
Contact Information for Business Card
Dorian Pelk
Director
0499827304
dorian@fixwelltechrepairs.example
3/27 Wendale Place, Burleigh Heads QLD 4220
Logo Text
Fixwell Tech Repairs
Requirements
Must have
- Small icon elements where required and Quibbit, Pavlora, Work Nest icons just so people recognise there are other methods of communication.
- Back side of card to have space to write name, number and details with light shade lines
Nice to have
- clean bright look with colour

```html
<!DOCTYPE html>
<html lang="en">
<head>
<meta charset="utf-8">
<title>Fixwell Tech Repairs – Business Card</title>
<link href="https://fonts.googleapis.com/css2?family=Bebas+Neue&family=Open+Sans:wght@400;600&display=swap" rel="stylesheet">
<style>
  :root {
    --page: #fefefe;
    --card-white: #fdfdfd;
    --charcoal: #232325;
    --panel: #222224;
    --lime: #8dc63f;
    --ink: #231f20;
    --line: #4a4a4a;
    --text-light: #ffffff;
  }
  * { margin: 0; padding: 0; box-sizing: border-box; }
  html, body {
    width: 1200px; height: 1000px; overflow: hidden;
    background: var(--page);
    font-family: "Open Sans", sans-serif;
  }
  .card {
    position: absolute; left: 241px; top: 251px;
    width: 714px; height: 409px;
    background: var(--charcoal);
  }
  .card__face {
    position: absolute; left: 0; top: 0;
    width: 520px; height: 270px;
    background: var(--card-white);
    border: 1px solid var(--line);
    border-right: none;
  }
  .card__accent-band {
    position: absolute; left: 0; top: 270px;
    width: 520px; height: 13px;
    background: var(--lime);
  }
  .card__name-panel {
    position: absolute; left: 520px; top: 0;
    width: 194px; height: 329px;
    background: var(--panel);
  }
  .card__stripe {
    position: absolute; left: 610px; width: 15px;
    background: var(--lime);
  }
  .card__stripe--top { top: 0; height: 144px; }
  .card__stripe--bottom { top: 235px; height: 174px; }
  .brand {
    position: absolute; left: 30px; top: 80px;
    display: flex; align-items: center; gap: 10px;
  }
  .brand__mark { width: 22px; height: 22px; background: var(--lime); }
  .brand__name {
    font-weight: 600; font-size: 26px; color: var(--ink);
    letter-spacing: -0.5px;
  }
  .person {
    position: absolute; left: 520px; top: 161px;
    width: 194px; text-align: center;
  }
  .person__name {
    font-family: "Bebas Neue", sans-serif;
    font-size: 38px; line-height: 36px; color: var(--text-light);
    letter-spacing: 0.3px;
  }
  .person__name-last { color: var(--lime); }
  .person__role {
    font-size: 17px; line-height: 20px; color: var(--text-light);
    margin-left: -8px;
  }
  .contacts {
    position: absolute; left: 30px; top: 299px;
    list-style: none;
  }
  .contacts__item {
    display: flex; align-items: center; gap: 6px;
    height: 24px;
    font-size: 13px; color: var(--text-light);
  }
  .contacts__icon { width: 17px; height: 17px; flex: none; }
</style>
</head>
<body>
  <div class="card">
    <div class="card__face">
      <div class="brand">
        <span class="brand__mark"></span>
        <span class="brand__name">Fixwell Tech Repairs</span>
      </div>
    </div>
    <div class="card__accent-band"></div>
    <div class="card__name-panel"></div>
    <div class="card__stripe card__stripe--top"></div>
    <div class="card__stripe card__stripe--bottom"></div>

    <div class="person">
      <div class="person__name">Dorian <span class="person__name-last">Pelk</span></div>
      <div class="person__role">DIRECTOR</div>
    </div>

    <ul class="contacts">
      <li class="contacts__item">
        <svg class="contacts__icon" viewBox="0 0 17 17"><rect width="17" height="17" rx="3" fill="#fff"/><circle cx="8.5" cy="8.5" r="6" fill="none" stroke="#232325" stroke-width="1.2"/><path d="M6 5.2l1.4-.4.9 2-1 .7c.4 1 1.1 1.7 2 2.1l.7-1 2 .9-.4 1.4c-3 .3-6-2.7-5.6-5.7z" fill="#232325"/></svg>
        0499827304
      </li>
      <li class="contacts__item">
        <svg class="contacts__icon" viewBox="0 0 17 17"><rect width="17" height="17" rx="3" fill="#fff"/><g fill="none" stroke="#232325" stroke-width="1.1"><circle cx="8.5" cy="8.5" r="5.8"/><ellipse cx="8.5" cy="8.5" rx="2.6" ry="5.8"/><path d="M2.7 8.5h11.6M3.6 5.6h9.8M3.6 11.4h9.8"/></g></svg>
        www.fixwelltechrepairs.example
      </li>
      <li class="contacts__item">
        <svg class="contacts__icon" viewBox="0 0 17 17"><rect width="17" height="17" rx="3" fill="#fff"/><rect x="2.5" y="4.5" width="12" height="8" fill="none" stroke="#232325" stroke-width="1.2"/><path d="M2.5 4.5l6 4.5 6-4.5M2.5 12.5l4.5-4M14.5 12.5l-4.5-4" fill="none" stroke="#232325" stroke-width="1.1"/></svg>
        dorian@fixwelltechrepairs.example
      </li>
      <li class="contacts__item">
        <svg class="contacts__icon" viewBox="0 0 17 17"><rect width="17" height="17" rx="3" fill="#fff"/><path d="M2.5 9L8.5 3.2 14.5 9h-2v5h-3v-3.2h-2V14h-3V9z" fill="#232325"/></svg>
        3 / 27 Wendale Place, Marrowby Heads KV 9071
      </li>
    </ul>
  </div>
</body>
</html>
```